■依頼の目的/概要
当方販促で使用するメモ帳を販売しております。
今回は年末年始に企業様が挨拶に出向く時に使用するノベルティメモ帳の表紙及び本文のデザインをお願いします。

■依頼詳細
表紙に和柄がデザインされ、組み立てるとカレンダーとして使える表紙のデザインをお願いします。使われる企業様は全国の企業様さまざまです。過去3年の実績デザインを添付しております。昨年も多数の提案がありました。採用に迷ったデザインも多数ありました。内容が変わらない提案でも歓迎です。

■重視するポイント
色使いなど制限はありませんが、和柄の縁起の良いデザインを希望いたします。テンプレートを添付しておりますのでご利用下さい。

その他何かご不明な点がございましたら、お気軽にご質問下さい。
よろしくお願いいたします。

社内アンケートを行って決定しました。上品でおめでたいイメージのものが選ばれたように思います。

今回の依頼でたくさんのランサーの皆様のご提案ありがとうございます。せっかく時間を割いて提案して下さったにも関わらず選択されなかったランサー様には申し訳けなく思っております。また来年も募集いたします。よろしければご提案下さいませ。

```html
<!DOCTYPE html>
<html lang="ja">
<head>
<meta charset="utf-8">
<title>2019 和柄カレンダー表紙 テンプレート</title>
<link rel="stylesheet" href="https://fonts.googleapis.com/css2?family=Noto+Sans+JP:wght@400&family=Roboto+Mono:wght@500&family=Cinzel:wght@500&display=swap">
<style>
  :root {
    --paper: #ffffff;
    --page-bg: #ffffff;
    --crimson: #c21d48;
    --crimson-deep: #a8123a;
    --blush: #f6d9df;
    --gold: #b8924a;
    --ink: #222222;
    --sunday: #c8202f;
    --trim: #9a9a9a;
    --fold: #c77a8e;
  }
  html, body {
    margin: 0;
    padding: 0;
    width: 849px;
    height: 1200px;
    overflow: hidden;
    background: var(--page-bg);
  }
  .sheet { display: block; width: 849px; height: 1200px; }
  .panel-label {
    font-family: "Noto Sans JP", sans-serif;
    font-size: 13px;
    fill: var(--ink);
  }
  .trim-mark { stroke: var(--trim); stroke-width: 0.8; fill: none; }
  .fold-line { stroke: var(--fold); stroke-width: 0.8; fill: none; }
  .band-rule { stroke: #e6c27a; stroke-width: 1.2; fill: none; }
  .year-gold {
    font-family: "Cinzel", serif;
    fill: var(--gold);
  }
  .cal-month {
    font-family: "Roboto Mono", monospace;
    font-size: 11px;
    font-weight: 500;
    fill: var(--crimson);
  }
  .cal-days {
    font-family: "Roboto Mono", monospace;
    font-size: 7px;
    font-weight: 500;
    fill: var(--ink);
    white-space: pre;
  }
  .cal-head { fill: var(--sunday); }
</style>
</head>
<body>
<svg class="sheet" viewBox="0 0 849 1200" xmlns="http://www.w3.org/2000/svg">
  <defs>
    <linearGradient id="front-top-bg" x1="0" y1="0" x2="1" y2="1">
      <stop offset="0" stop-color="#f3c9d3"/>
      <stop offset="0.5" stop-color="#fbeef1"/>
      <stop offset="1" stop-color="#ffffff"/>
    </linearGradient>
    <linearGradient id="front-bottom-bg" x1="0" y1="0" x2="0" y2="1">
      <stop offset="0" stop-color="#f7dfe4"/>
      <stop offset="0.35" stop-color="#e8889d"/>
      <stop offset="1" stop-color="#c21d48"/>
    </linearGradient>
    <linearGradient id="inner-top-bg" x1="0" y1="0" x2="0" y2="1">
      <stop offset="0" stop-color="#d6e4f4"/>
      <stop offset="1" stop-color="#ffffff"/>
    </linearGradient>
    <linearGradient id="inner-bottom-bg" x1="0" y1="0" x2="0" y2="1">
      <stop offset="0" stop-color="#ffffff"/>
      <stop offset="0.45" stop-color="#f4d3da"/>
      <stop offset="1" stop-color="#c21d48"/>
    </linearGradient>
    <linearGradient id="pattern-band" x1="0" y1="0" x2="1" y2="0">
      <stop offset="0" stop-color="#a8123a"/>
      <stop offset="0.3" stop-color="#c9784e"/>
      <stop offset="0.55" stop-color="#b8234a"/>
      <stop offset="0.8" stop-color="#d39a5e"/>
      <stop offset="1" stop-color="#a8123a"/>
    </linearGradient>
    <linearGradient id="flower-main" x1="0" y1="0" x2="1" y2="1">
      <stop offset="0" stop-color="#f6c7d2"/>
      <stop offset="0.5" stop-color="#d23a5c"/>
      <stop offset="1" stop-color="#e2b86a"/>
    </linearGradient>
    <linearGradient id="flower-corner" x1="0" y1="0" x2="1" y2="1">
      <stop offset="0" stop-color="#f7d3dc"/>
      <stop offset="1" stop-color="#d9506f"/>
    </linearGradient>

    <symbol id="calendar-2019" viewBox="0 0 330 380">
      <g transform="translate(8,4)">
        <text class="cal-month" x="0" y="10">1</text>
        <text class="cal-days" y="22"><tspan x="0" class="cal-head"> S  M  T  W  T  F  S</tspan><tspan x="0" dy="9">       1  2  3  4  5</tspan><tspan x="0" dy="9"> 6  7  8  9 10 11 12</tspan><tspan x="0" dy="9">13 14 15 16 17 18 19</tspan><tspan x="0" dy="9">20 21 22 23 24 25 26</tspan><tspan x="0" dy="9">27 28 29 30 31</tspan></text>
      </g>
      <g transform="translate(118,4)">
        <text class="cal-month" x="0" y="10">2</text>
        <text class="cal-days" y="22"><tspan x="0" class="cal-head"> S  M  T  W  T  F  S</tspan><tspan x="0" dy="9">                1  2</tspan><tspan x="0" dy="9"> 3  4  5  6  7  8  9</tspan><tspan x="0" dy="9">10 11 12 13 14 15 16</tspan><tspan x="0" dy="9">17 18 19 20 21 22 23</tspan><tspan x="0" dy="9">24 25 26 27 28</tspan></text>
      </g>
      <g transform="translate(228,4)">
        <text class="cal-month" x="0" y="10">3</text>
        <text class="cal-days" y="22"><tspan x="0" class="cal-head"> S  M  T  W  T  F  S</tspan><tspan x="0" dy="9">                1  2</tspan><tspan x="0" dy="9"> 3  4  5  6  7  8  9</tspan><tspan x="0" dy="9">10 11 12 13 14 15 16</tspan><tspan x="0" dy="9">17 18 19 20 21 22 23</tspan><tspan x="0" dy="9">24 25 26 27 28 29 30</tspan><tspan x="0" dy="9">31</tspan></text>
      </g>
      <g transform="translate(8,98)">
        <text class="cal-month" x="0" y="10">4</text>
        <text class="cal-days" y="22"><tspan x="0" class="cal-head"> S  M  T  W  T  F  S</tspan><tspan x="0" dy="9">    1  2  3  4  5  6</tspan><tspan x="0" dy="9"> 7  8  9 10 11 12 13</tspan><tspan x="0" dy="9">14 15 16 17 18 19 20</tspan><tspan x="0" dy="9">21 22 23 24 25 26 27</tspan><tspan x="0" dy="9">28 29 30</tspan></text>
      </g>
      <g transform="translate(118,98)">
        <text class="cal-month" x="0" y="10">5</text>
        <text class="cal-days" y="22"><tspan x="0" class="cal-head"> S  M  T  W  T  F  S</tspan><tspan x="0" dy="9">          1  2  3  4</tspan><tspan x="0" dy="9"> 5  6  7  8  9 10 11</tspan><tspan x="0" dy="9">12 13 14 15 16 17 18</tspan><tspan x="0" dy="9">19 20 21 22 23 24 25</tspan><tspan x="0" dy="9">26 27 28 29 30 31</tspan></text>
      </g>
      <g transform="translate(228,98)">
        <text class="cal-month" x="0" y="10">6</text>
        <text class="cal-days" y="22"><tspan x="0" class="cal-head"> S  M  T  W  T  F  S</tspan><tspan x="0" dy="9">                   1</tspan><tspan x="0" dy="9"> 2  3  4  5  6  7  8</tspan><tspan x="0" dy="9"> 9 10 11 12 13 14 15</tspan><tspan x="0" dy="9">16 17 18 19 20 21 22</tspan><tspan x="0" dy="9">23 24 25 26 27 28 29</tspan><tspan x="0" dy="9">30</tspan></text>
      </g>
      <g transform="translate(8,192)">
        <text class="cal-month" x="0" y="10">7</text>
        <text class="cal-days" y="22"><tspan x="0" class="cal-head"> S  M  T  W  T  F  S</tspan><tspan x="0" dy="9">    1  2  3  4  5  6</tspan><tspan x="0" dy="9"> 7  8  9 10 11 12 13</tspan><tspan x="0" dy="9">14 15 16 17 18 19 20</tspan><tspan x="0" dy="9">21 22 23 24 25 26 27</tspan><tspan x="0" dy="9">28 29 30 31</tspan></text>
      </g>
      <g transform="translate(118,192)">
        <text class="cal-month" x="0" y="10">8</text>
        <text class="cal-days" y="22"><tspan x="0" class="cal-head"> S  M  T  W  T  F  S</tspan><tspan x="0" dy="9">             1  2  3</tspan><tspan x="0" dy="9"> 4  5  6  7  8  9 10</tspan><tspan x="0" dy="9">11 12 13 14 15 16 17</tspan><tspan x="0" dy="9">18 19 20 21 22 23 24</tspan><tspan x="0" dy="9">25 26 27 28 29 30 31</tspan></text>
      </g>
      <g transform="translate(228,192)">
        <text class="cal-month" x="0" y="10">9</text>
        <text class="cal-days" y="22"><tspan x="0" class="cal-head"> S  M  T  W  T  F  S</tspan><tspan x="0" dy="9"> 1  2  3  4  5  6  7</tspan><tspan x="0" dy="9"> 8  9 10 11 12 13 14</tspan><tspan x="0" dy="9">15 16 17 18 19 20 21</tspan><tspan x="0" dy="9">22 23 24 25 26 27 28</tspan><tspan x="0" dy="9">29 30</tspan></text>
      </g>
      <g transform="translate(8,286)">
        <text class="cal-month" x="0" y="10">10</text>
        <text class="cal-days" y="22"><tspan x="0" class="cal-head"> S  M  T  W  T  F  S</tspan><tspan x="0" dy="9">       1  2  3  4  5</tspan><tspan x="0" dy="9"> 6  7  8  9 10 11 12</tspan><tspan x="0" dy="9">13 14 15 16 17 18 19</tspan><tspan x="0" dy="9">20 21 22 23 24 25 26</tspan><tspan x="0" dy="9">27 28 29 30 31</tspan></text>
      </g>
      <g transform="translate(118,286)">
        <text class="cal-month" x="0" y="10">11</text>
        <text class="cal-days" y="22"><tspan x="0" class="cal-head"> S  M  T  W  T  F  S</tspan><tspan x="0" dy="9">                1  2</tspan><tspan x="0" dy="9"> 3  4  5  6  7  8  9</tspan><tspan x="0" dy="9">10 11 12 13 14 15 16</tspan><tspan x="0" dy="9">17 18 19 20 21 22 23</tspan><tspan x="0" dy="9">24 25 26 27 28 29 30</tspan></text>
      </g>
      <g transform="translate(228,286)">
        <text class="cal-month" x="0" y="10">12</text>
        <text class="cal-days" y="22"><tspan x="0" class="cal-head"> S  M  T  W  T  F  S</tspan><tspan x="0" dy="9"> 1  2  3  4  5  6  7</tspan><tspan x="0" dy="9"> 8  9 10 11 12 13 14</tspan><tspan x="0" dy="9">15 16 17 18 19 20 21</tspan><tspan x="0" dy="9">22 23 24 25 26 27 28</tspan><tspan x="0" dy="9">29 30 31</tspan></text>
      </g>
    </symbol>
  </defs>

  <text class="panel-label" x="42" y="62">表紙おもて・表紙うら</text>
  <text class="panel-label" x="448" y="62">表紙なか</text>

  <g class="cover-outer">
    <rect x="42" y="100" width="363" height="480" fill="url(#front-top-bg)"/>
    <path class="back-calendar-card" d="M62 100 H392 V530 H150 Q62 530 62 450 Z" fill="var(--paper)"/>
    <g class="back-calendar" transform="rotate(180 228 315)">
      <use href="#calendar-2019" x="78" y="175" width="290" height="320"/>
      <text class="year-gold" x="216" y="160" font-size="24">2019</text>
    </g>
    <circle role="img" aria-label="梅の花と水引の和風イラスト" cx="88" cy="500" r="42" fill="url(#flower-corner)"/>

    <rect role="img" aria-label="金と赤の和柄帯" x="42" y="580" width="363" height="96" fill="url(#pattern-band)"/>
    <path class="band-rule" d="M42 584 H405 M42 672 H405"/>

    <rect x="42" y="676" width="363" height="442" fill="url(#front-bottom-bg)"/>
    <text class="year-gold" x="62" y="762" font-size="34">2019</text>
    <ellipse role="img" aria-label="紅白の梅と金の水引、椿の和風イラスト" cx="228" cy="910" rx="118" ry="140" fill="url(#flower-main)"/>
  </g>

  <g class="cover-inner">
    <rect x="444" y="100" width="362" height="423" fill="url(#inner-top-bg)"/>
    <rect role="img" aria-label="金と赤の和柄帯" x="444" y="523" width="362" height="77" fill="url(#pattern-band)"/>
    <path class="band-rule" d="M444 527 H806 M444 596 H806"/>
    <rect class="calendar-card" x="523" y="240" width="255" height="290" rx="10" fill="var(--paper)"/>
    <text class="year-gold" x="650" y="268" font-size="16" text-anchor="middle" fill="var(--crimson)">2019</text>
    <use href="#calendar-2019" x="530" y="276" width="242" height="240"/>

    <rect x="444" y="600" width="362" height="518" fill="url(#inner-bottom-bg)"/>
    <line class="fold-line" x1="444" y1="600" x2="806" y2="600"/>
    <path class="fold-line" d="M590 708 Q625 722 660 708"/>
  </g>

  <g class="trim-marks">
    <path class="trim-mark" d="M42 72 V92 M405 72 V92 M22 100 H34 M413 100 H427"/>
    <path class="trim-mark" d="M42 1126 V1146 M405 1126 V1146 M22 1118 H34 M413 1118 H427"/>
    <path class="trim-mark" d="M444 72 V92 M806 72 V92 M430 100 H436 M814 100 H830"/>
    <path class="trim-mark" d="M444 1126 V1146 M806 1126 V1146 M430 1118 H436 M814 1118 H830"/>
    <path class="trim-mark" d="M14 600 H34 M814 600 H836 M223 72 V92 M625 72 V92 M223 1126 V1146 M625 1126 V1146"/>
    <rect class="trim-mark" x="42" y="100" width="363" height="1018"/>
    <rect class="trim-mark" x="444" y="100" width="362" height="1018"/>
  </g>
</svg>
</body>
</html>
```